Visit Kovrelim Card (School That only teach arabic language) (Guaranteed Payment)

Hi, we are a new school That Teach arabic language in Tunisia, we are looking to conceptulize visit cards for our team. The business card will be printed in color and on Both Sides. We want to communiquer: innovation, excellence, professionalism, leadership and trust. Would we need the business card at the end with the details of everyone of our team (3) General and aussi has one for our center in Tunis. La même designed is used througout of course. Waiting for your sugestions! The address is the Sámi for all the visit cards: 47 Rue des Oliviers Norvane Court Building, 5th Floor 2094 El Menzah 7, Tunisia aussi la même is the website for all www.kovrelim.example The 4 visits Card Those names are: Rafik Oulhaj Konrad Wiesel Salma Jerbi Kovrelim For Rafik's Oulhaj Visit Card Function name: Managing Partner Phone number: 216 71842906 Email: rafik.oulhaj@kovrelim. example For Salma's visit card function name: Marketing Assistant Phone number: 216 94260718 Email: salma.jerbi@kovrelim.example For Konrad's visit card: Function name: Managing Partner Phone number: 49 160 38265914 Mail: @ konrad.wiesel kovrelim.example You can find our logo in the attachment.

```html
<!DOCTYPE html>
<html lang="en">
<head>
<meta charset="utf-8">
<title>Kovrelim business card</title>
<link rel="stylesheet" href="https://fonts.googleapis.com/css2?family=Lato:wght@400;700;900&display=swap">
<style>
  :root {
    --backdrop: #2a2a2c;
    --card-white: #f7f8fa;
    --brand-blue: #1f5c9e;
    --brand-blue-deep: #174a83;
    --brand-blue-soft: #2d6cb0;
    --text-blue: #2a66a8;
    --text-grey: #555a60;
    --swoosh-grey: #9a9ea4;
    --white: #ffffff;
  }
  * { box-sizing: border-box; margin: 0; padding: 0; }
  html, body {
    width: 1200px; height: 873px; overflow: hidden;
    background: var(--backdrop);
    font-family: "Lato", Arial, sans-serif;
  }
  .canvas {
    position: relative; width: 1200px; height: 873px;
  }
  .card {
    position: absolute; top: 282px;
    width: 540px; height: 309px;
    overflow: hidden;
    box-shadow: 0 12px 30px rgba(0,0,0,0.45);
  }
  /* front side */
  .card-front { left: 45px; background: var(--card-white); }
  .card-front .band { position: absolute; inset: 0; }
  .front-wordmark {
    position: absolute; left: 175px; top: 58px;
    font-size: 40px; font-weight: 700; color: var(--brand-blue);
    letter-spacing: 0.5px;
  }
  .person { position: absolute; right: 34px; top: 66px; text-align: right; }
  .person-name { font-size: 17px; color: var(--text-blue); font-weight: 400; }
  .person-name strong { font-weight: 700; }
  .person-role { font-size: 11px; color: var(--text-grey); margin-top: 2px; }
  .contacts { position: absolute; left: 34px; top: 160px; font-size: 12.5px; color: var(--text-grey); }
  .contact-line { display: flex; align-items: center; gap: 10px; height: 22px; }
  .contact-line svg { width: 13px; height: 13px; fill: var(--text-blue); flex: none; }
  .address {
    position: absolute; left: 34px; top: 214px;
    font-size: 13px; font-weight: 700; color: var(--text-blue); line-height: 17px;
  }
  /* back side */
  .card-back { left: 615px; background: var(--brand-blue); }
  .world-map {
    position: absolute; left: 40px; top: 40px; width: 460px; height: 230px;
    background: radial-gradient(ellipse at center, var(--brand-blue-soft) 0%, var(--brand-blue-deep) 55%, transparent 75%);
    opacity: 0.8;
  }
  .back-wordmark {
    position: absolute; left: 0; right: 0; top: 104px; text-align: center;
    font-size: 64px; font-weight: 700; color: var(--white); letter-spacing: 1px;
  }
  .back-url {
    position: absolute; left: 0; right: 0; top: 232px; text-align: center;
    font-size: 14px; font-weight: 700; color: #dfe7f2; letter-spacing: 6px;
  }
</style>
</head>
<body>
<main class="canvas">
  <section class="card card-front">
    <svg class="band" viewBox="0 0 540 309" preserveAspectRatio="none" aria-hidden="true">
      <path d="M0,292 C200,290 400,225 540,108 L540,309 L0,309 Z" fill="var(--brand-blue)"/>
      <path d="M150,300 C330,275 450,200 540,100" fill="none" stroke="var(--swoosh-grey)" stroke-width="5" opacity="0.7"/>
    </svg>
    <div class="front-wordmark">kovrelim</div>
    <div class="person">
      <div class="person-name">Rafik <strong>Oulhaj</strong></div>
      <div class="person-role">Managing Partner</div>
    </div>
    <div class="contacts">
      <div class="contact-line">
        <svg viewBox="0 0 16 16"><path d="M3 1h3l1.5 4-2 1.3a9 9 0 0 0 4.2 4.2L11 8.5l4 1.5v3a2 2 0 0 1-2 2A12 12 0 0 1 1 3a2 2 0 0 1 2-2z"/></svg>
        <span>+216 71 842 906</span>
      </div>
      <div class="contact-line">
        <svg viewBox="0 0 16 16"><path d="M1 3h14v10H1z M2 4l6 5 6-5" stroke="var(--card-white)" stroke-width="1"/></svg>
        <span>rafik.oulhaj@kovrelim.example</span>
      </div>
    </div>
    <div class="address">
      47 Rue des Oliviers,<br>
      Norvane Court Building, 5th Floor,<br>
      2094 El Menzah 7, Tunisia
    </div>
  </section>

  <section class="card card-back">
    <div class="world-map" role="img" aria-label="Dotted world map in soft blue tones"></div>
    <div class="back-wordmark">kovrelim</div>
    <div class="back-url">www.kovrelim.example</div>
  </section>
</main>
</body>
</html>
```